Wordpress Design Project - Development Company

We need a website for our Developments company "KT Developments". I would like to use Wordpress for its simplicity to update and added features.
We develop/build and sell Townhouses/Houses and Land around Brisbane, Qld. Initially we require a Web presence with no advanced features. We will develop the user logins and other features at a future point in time. We are undecided on having a single page with most of the detail or to have more detail on linked pages, we will review the options put forward. We have added a Sitemap and possible Frontpage sketch
Some sites for examples we have thought work similar and well:
http://www.brimfield.com.au/index.htm
http://tallowmeadow.com.au/
http://www.pmcorrigan.com.au
http://nexcrafta.com.au/
http://www.halvery.com.au/queensland.aspx
http://www.orbelyne.com.au/
I've attached our newly created Business Cards and we are also working on a logo for the company within the next couple of days which may or may not be the same as the Business Card
Any questions please ask
Updates
Please update the main picture on your webpages to the attached so we can compare equally http://files.quillbox.net/u/55720194/Img1c.jpg
Target Market(s)
Townhouse/House/Land buyers & Salespeople
Industry/Entity Type
Business
Look and feel

```html
<!DOCTYPE html>
<html lang="en">
<head>
<meta charset="utf-8">
<title>KT Developments P/L</title>
<link rel="stylesheet" href="https://fonts.googleapis.com/css2?family=Arimo:wght@400;700&family=Open+Sans:wght@400;600;700&family=Oswald:wght@400&family=Great+Vibes&display=swap">
<style>
:root{
  --red:#a01c2a;
  --red-dark:#7e1420;
  --ink:#222;
  --text:#444;
  --muted:#999;
  --nav:#333;
  --page:#ffffff;
}
*{box-sizing:border-box;margin:0;padding:0}
html,body{width:1074px;height:1200px;overflow:hidden}
body{position:relative;background:var(--page);font-family:"Arimo",Arial,sans-serif;color:var(--text)}
.abs{position:absolute}
ul{list-style:none}

.header{left:0;top:0;width:1074px;height:169px;background:linear-gradient(180deg,#ececec 0%,#f8f8f8 55%,#e9e9e9 100%)}
.brand{left:52px;top:40px;font-family:"Arimo",Arial,sans-serif;font-weight:700;font-size:30px;color:#222;line-height:1;white-space:nowrap}
.call{right:60px;top:14px;font-family:"Oswald",sans-serif;font-size:38px;color:#555;letter-spacing:-.5px}
.call b{font-weight:400;color:var(--red)}
.util{right:64px;top:80px;display:flex;gap:29px;font-size:12px;font-weight:700;color:#444}
.nav{left:0;top:124px;width:1074px;height:30px;font-family:"Arimo",Arial,sans-serif;font-weight:700;font-size:14px;color:var(--nav)}
.nav li{position:absolute;top:0;height:30px;line-height:30px;white-space:nowrap}
.nav li.active{background:#7a7a7a;color:#fff;padding:0 8px}

.band{left:0;top:169px;width:1074px;height:406px}
.slide{left:97px;top:202px;width:880px;height:340px;border-radius:6px;overflow:hidden;box-shadow:0 6px 14px rgba(0,0,0,.35)}
.slide-photo{position:absolute;inset:0;background:linear-gradient(180deg,#f4f8fb 0%,#dfe9ef 38%,#7f9a58 62%,#5c7d2e 100%)}
.slide-title{position:absolute;left:55px;top:170px;font-family:"Great Vibes",cursive;font-size:62px;color:#fff;text-shadow:0 2px 4px rgba(0,0,0,.4)}
.slide-caption{position:absolute;left:20px;top:277px;width:840px;font-family:"Open Sans",sans-serif;font-size:13px;line-height:22px;color:#fff;text-transform:uppercase}
.arrow{top:354px;width:28px;height:35px;background:#fff;border-radius:3px;box-shadow:0 1px 3px rgba(0,0,0,.4)}

.contact-card{left:62px;top:589px;width:214px;height:294px;background:#fff;border:1px solid #ccc;box-shadow:0 0 0 3px #eee}
.contact-head{height:38px;background:linear-gradient(180deg,#6a6a6a,#2f2f2f);color:#fff;font-family:"Open Sans",sans-serif;font-weight:600;font-size:20px;line-height:38px;padding-left:11px}
.contact-body{padding:14px 11px 0;font-size:14px;line-height:18px;color:#111}
.contact-body dt{margin-top:10px}
.contact-body dt:first-child{margin-top:0}
.contact-body dd{color:#333}
.contact-body .addr{font-size:12px;line-height:18px;width:128px;color:#555}
.rep-photo{left:222px;top:709px;width:54px;height:160px;background:linear-gradient(180deg,#d8d8d8,#8a8a8a)}
.click{left:173px;top:871px;width:95px;height:23px;background:var(--red);color:#fff;font-size:13px;line-height:23px;text-align:center}

.welcome{left:294px;top:592px;width:718px}
.welcome h1{font-family:"Open Sans",sans-serif;font-weight:700;font-size:20px;color:var(--red);padding-bottom:6px;border-bottom:1px dotted #bbb}
.welcome p{font-size:13px;line-height:19px;color:#999;margin-top:10px}

.project{top:726px;width:204px}
.project h2{font-family:"Open Sans",sans-serif;font-weight:600;font-size:14px;color:#333;margin-bottom:10px}
.project .thumb{height:68px}
.project ul{margin-top:18px;font-size:12px;color:#333}
.project li{height:26px;padding-left:12px;position:relative;white-space:nowrap}
.project li::before{content:"›";position:absolute;left:0;top:-3px;color:var(--red);font-size:15px}

.footer{left:0;top:975px;width:1074px;height:170px;background:linear-gradient(180deg,#e4e4e4,#f3f3f3)}
.footer h3{font-size:12px;font-weight:700;color:var(--red);margin-bottom:10px}
.footer li{font-size:12px;color:#555;height:26px;padding-left:12px;position:relative}
.footer .links li::before{content:"›";position:absolute;left:0;top:-2px;color:#777;font-size:14px}
.footer .reach li{padding-left:0;height:22px}
.mailing{left:758px;top:975px;width:316px;height:170px;background:#f7f7f7}
.mailing h3{font-family:"Open Sans",sans-serif;font-size:20px;font-weight:700;color:var(--red);margin:13px 0 12px 18px}
.mailing p{font-size:12px;line-height:18px;color:#777;margin-left:18px;width:252px}
.nobr{white-space:nowrap}
.signup{position:absolute;left:17px;top:114px;width:247px;height:30px;border-radius:15px;background:linear-gradient(180deg,#fff,#ddd);border:1px solid #c8c8c8;font-size:12px;line-height:28px;padding-left:13px;color:#333}
.signup span{position:absolute;right:-1px;top:-1px;width:78px;height:30px;border-radius:15px;background:var(--red);color:#fff;text-align:center;line-height:30px}

.legal{left:0;top:1145px;width:1074px;height:55px;background:#fff;border-top:1px solid #ddd}
.legal p{position:absolute;left:57px;top:15px;font-size:12px;color:#555}
.social{position:absolute;top:15px;width:16px;height:16px;border-radius:2px}
</style>
</head>
<body>

<header class="abs header">
  <svg class="abs" width="1074" height="169" style="left:0;top:0" aria-hidden="true">
    <path d="M300 0 C500 80 800 40 1074 90 L1074 0Z" fill="#fff" opacity=".5"/>
  </svg>
</header>
<div class="abs brand">KT Developments P/L</div>
<div class="abs call">CALL <b>3927 4105</b></div>
<ul class="abs util"><li>Home</li><li>Sitemap</li><li>Disclaimer/Privacy Policy</li></ul>
<ul class="abs nav">
  <li class="active" style="left:48px">OVERVIEW</li>
  <li style="left:178px">CURRENT PROJECTS</li>
  <li style="left:372px">COMPLETED PROJECTS</li>
  <li style="left:586px">FUTURE PROJECTS</li>
  <li style="left:768px">LATEST NEWS</li>
  <li style="left:915px">CONTACT US</li>
</ul>

<svg class="abs band" width="1074" height="406" aria-hidden="true">
  <defs>
    <linearGradient id="bandFill" x1="0" x2="0" y1="0" y2="1">
      <stop offset="0" stop-color="#8d1c29"/><stop offset=".5" stop-color="#a72b38"/><stop offset="1" stop-color="#8d1c29"/>
    </linearGradient>
  </defs>
  <rect width="1074" height="406" fill="#f0f0f0"/>
  <path d="M0 0 Q537 -20 1074 0 L1074 406 Q537 380 0 406Z" fill="url(#bandFill)"/>
  <rect x="0" y="0" width="48" height="406" fill="#000" opacity=".08"/>
  <rect x="1026" y="0" width="48" height="406" fill="#000" opacity=".08"/>
</svg>
<div class="abs slide">
  <div class="slide-photo" role="img" aria-label="Photo of a family running across a sunlit lawn with balloons"></div>
  <div class="slide-title">A New light on living</div>
  <p class="slide-caption">Lorem Ipsum is simply dummy text of the printing and typesetting industry. Lorem Ipsum has been the industry's standard dummy text ever since the 1500s...</p>
</div>
<svg class="abs arrow" style="left:68px" viewBox="0 0 28 35" aria-label="Previous"><path d="M17 10 L10 17.5 L17 25" stroke="#8d1c29" stroke-width="4" fill="none"/></svg>
<svg class="abs arrow" style="left:977px" viewBox="0 0 28 35" aria-label="Next"><path d="M11 10 L18 17.5 L11 25" stroke="#8d1c29" stroke-width="4" fill="none"/></svg>

<aside class="abs contact-card">
  <div class="contact-head">CONTACT US</div>
  <dl class="contact-body">
    <dt>Phone</dt><dd>3927 4105</dd>
    <dt>Mobile</dt><dd>0431 662 908</dd>
    <dt>Email</dt><dd>sales@ktdev.com</dd>
    <dt>Address</dt><dd class="addr">Lorem Ipsum is simply dummy text of the printing &amp; typesetting</dd>
  </dl>
</aside>
<div class="abs rep-photo" role="img" aria-label="Photo of a sales representative in a suit"></div>
<div class="abs click">CLICK HERE ›</div>

<section class="abs welcome">
  <h1>WELCOME TO KT DEVELOPMENTS P/L</h1>
  <p>Lorem Ipsum is simply dummy text of the printing and typesetting industry. Lorem Ipsum has been the industry's standard dummy text ever since the 1500s, when an unknown printer took a galley of type and scrambled it to make a type specimen book.</p>
</section>

<section class="abs project" style="left:294px">
  <h2>CURRENT PROJECTS</h2>
  <div class="thumb" role="img" aria-label="Photo of a modern townhouse block" style="background:linear-gradient(180deg,#b9d3ea,#d9d9d9 60%,#8f9a8a)"></div>
  <ul><li>Fusce id magna metus, ut interdum</li><li>Duis in eros in ipsum porttitor mattis</li><li>Etiam ac urna id velit eleifend ultric</li></ul>
</section>
<section class="abs project" style="left:551px">
  <h2>COMPLETED PROJECTS</h2>
  <div class="thumb" role="img" aria-label="Photo of a family relaxing at home" style="background:linear-gradient(90deg,#f2e6dc,#e3c9b2 50%,#f4ece4)"></div>
  <ul><li>Fusce id magna metus, ut interdum</li><li>Duis in eros in ipsum porttitor mattis</li><li>Etiam ac urna id velit eleifend ultric</li></ul>
</section>
<section class="abs project" style="left:809px">
  <h2>FUTURE PROJECTS</h2>
  <div class="thumb" role="img" aria-label="Photo of a suburban street of new houses" style="background:linear-gradient(180deg,#e9d7b8,#b89a72 55%,#8a8f5a)"></div>
  <ul><li>Fusce id magna metus, ut interdum</li><li>Duis in eros in ipsum porttitor mattis</li><li>Etiam ac urna id velit eleifend ultric</li></ul>
</section>
<svg class="abs" width="4" height="130" style="left:523px;top:745px" aria-hidden="true"><rect width="2" height="130" fill="#ececec"/></svg>
<svg class="abs" width="4" height="130" style="left:781px;top:745px" aria-hidden="true"><rect width="2" height="130" fill="#ececec"/></svg>

<footer class="abs footer">
  <div class="abs links" style="left:58px;top:20px">
    <h3>Latest News</h3>
    <ul><li>Nam ac velit neque, at elementum quam.</li><li>Nulla mollis erat et ipsum convallis id dapibus massa</li><li>Morbi fringilla quam sit amet dui tempus facilisis.</li><li>Morbi facilisis augue non mauris dapibus tristique.</li></ul>
  </div>
  <div class="abs links" style="left:402px;top:20px">
    <h3>Quick Links</h3>
    <ul><li>Overview</li><li>Current Projects</li><li>Completed Projects</li><li>Future Projects</li></ul>
  </div>
  <div class="abs reach" style="left:571px;top:20px">
    <h3>How to reach us</h3>
    <ul><li>Phone: 3927 4105</li><li>Mobile: 0431 662 908</li><li>Email: sales@ktdev.com</li><li>PO Box 2740</li><li>Marlow Heights QLD 4112</li></ul>
  </div>
</footer>
<section class="abs mailing">
  <h3>JOIN THE MAILING LIST</h3>
  <p>Users avoid filling out forms and submitting their details if possible. For a newsletter <span class="nobr">sign-ups,</span> all you need is their email address.</p>
  <div class="signup">Enter your email address<span>Sign Up »</span></div>
</section>

<div class="abs legal">
  <p>Copyright © 2011 KT Developments P/L. &nbsp;Disclaimer &nbsp;&nbsp;| &nbsp;&nbsp;Privacy Policy</p>
  <span class="social" style="left:954px;background:#3b5998"></span>
  <span class="social" style="left:977px;background:#3fb0e0"></span>
  <span class="social" style="left:1001px;background:#2a72a8"></span>
</div>

</body>
</html>
```